Postcard - We customize work clothing with your company name and/or logo

We customize work apparel for small to medium sized companies. We supply and customize most name brand tee shirts, polo shirts, dress shirts and hats with company name and logo. We also supply flame resistant shirts, coats, jeans, coveralls. We also make custom decals and stickers.We offer buying and ordering options catering to our customer’s needs. Explore the possibilities of custom apparel for uniforming, special events, team building and more. Give your organization an exceptional look with customized apparel designed for a lasting impact. Picture of Tee shirt with company name and logo goes here Picture of Polo shirt with company name and logo goes here Picture of Coveralls with name and logo Picture of a Base ball hat with company name and logo goes here. 10% off and no setup Fees with this promotional code – K-382

Target Market(s)

Small to medium sized companies

Industry/Entity Type

Clothing

Requirements
Must have
• The company name:
• Under The Lantern Tailored Garments and Extras, LLC
• 27852 Falvinter Road
• Cypress, Texas 77519
• Tel. (281) 555-0187
• email: underthelantern@mailtrove.example
• Web page: www.tailoredgarmentsandextras.example
• Web page: www.underthelantern.example

```html
<!DOCTYPE html>
<html lang="en">
<head>
<meta charset="utf-8">
<title>Under The Lantern – Custom Apparel Postcard</title>
<link rel="stylesheet" href="https://fonts.googleapis.com/css2?family=Teko:wght@500;600&family=Play:wght@400;700&display=swap">
<style>
  :root {
    --page-bg: #c6c5b9;
    --navy: #1f3a8c;
    --red: #d3202b;
    --gold-text: #a98c3c;
    --yellow: #ffd400;
    --yellow-light: #fff9df;
    --wave-green: #0d5a43;
    --blue-deep: #1a56b8;
    --blue-light: #13b4ee;
    --promo-yellow: #ffe600;
    --ink: #1d1d1d;
  }
  * { margin: 0; padding: 0; box-sizing: border-box; }
  html, body { width: 1200px; height: 1200px; overflow: hidden; }
  body { background: var(--page-bg); position: relative; font-family: "Play", sans-serif; }

  .postcard {
    position: absolute; left: 20px; top: 150px;
    width: 1160px; height: 900px; overflow: hidden;
    background: linear-gradient(180deg, var(--yellow-light) 0%, #fff1a0 30%, var(--yellow) 80%);
    box-shadow: 0 6px 18px rgba(0,0,0,.25);
  }
  .backdrop { position: absolute; inset: 0; }

  .headline { position: absolute; left: 38px; top: 34px; font-family: "Teko", sans-serif; font-weight: 600; color: var(--navy); line-height: .98; }
  .headline .lead { font-size: 48px; display: block; text-transform: uppercase; }
  .headline .feature { font-size: 78px; color: var(--red); display: block; letter-spacing: .5px; line-height: .9; margin: 4px 0 6px; }
  .headline .purpose { font-size: 46px; display: block; }

  .chevrons { position: absolute; left: 548px; top: 68px; }

  .service-list { position: absolute; left: 612px; top: 68px; list-style: none; font-size: 29px; color: var(--ink); line-height: 33px; }
  .service-list li { position: relative; padding-left: 26px; }
  .service-list li::before { content: "•"; position: absolute; left: 0; font-size: 20px; }

  .welcome { position: absolute; right: 640px; top: 415px; text-align: right; font-size: 35px; color: var(--gold-text); line-height: 40px; text-transform: uppercase; }

  .product { position: absolute; border-radius: 4px; }
  .product.tee { left: 985px; top: 55px; width: 115px; height: 135px; background: linear-gradient(180deg,#2a2a2a,#0d0d0d); }
  .product.polo { left: 975px; top: 205px; width: 125px; height: 160px; background: linear-gradient(180deg,#ffffff,#e6e6ea); }
  .product.coveralls { left: 955px; top: 380px; width: 165px; height: 170px; background: linear-gradient(180deg,#8a8560,#6b6747); }
  .product.cap { left: 985px; top: 565px; width: 100px; height: 80px; background: linear-gradient(180deg,#2b2b2b,#0f0f0f); border-radius: 50% 50% 20% 20%; }

  .promo { position: absolute; left: 20px; top: 655px; width: 300px; text-align: center; color: #fff; font-size: 37px; line-height: 40px; }
  .promo .discount { color: var(--promo-yellow); font-size: 62px; line-height: 62px; display: block; }

  .brand { position: absolute; right: 32px; top: 782px; display: flex; align-items: center; gap: 10px; }
  .brand .mark { width: 32px; height: 32px; border-radius: 50%; border: 3px solid var(--navy); flex: none; }
  .brand .name { font-size: 18px; line-height: 21px; color: var(--navy); font-weight: 700; }

  .contact { position: absolute; right: 270px; top: 840px; text-align: right; font-size: 16px; line-height: 18px; color: var(--ink); }
  .address { position: absolute; right: 32px; top: 840px; text-align: right; font-size: 16px; line-height: 18px; color: var(--ink); }
</style>
</head>
<body>
  <article class="postcard">
    <svg class="backdrop" width="1160" height="900" viewBox="0 0 1160 900" aria-hidden="true">
      <path d="M300,900 C430,820 540,770 720,745 C880,722 980,668 1160,660 L1160,900 Z" fill="var(--wave-green)"/>
      <path d="M330,900 C460,840 560,792 730,768 C885,745 985,692 1160,684 L1160,900 Z" fill="#ffffff"/>
      <defs>
        <linearGradient id="burst-fill" x1="0" y1="1" x2="1" y2="0">
          <stop offset="0" stop-color="var(--blue-light)"/>
          <stop offset="1" stop-color="var(--blue-deep)"/>
        </linearGradient>
      </defs>
      <polygon fill="#2a8fe0" stroke="#2a8fe0" stroke-width="34" stroke-linejoin="round"
        points="410,770 373,824 378,890 318,918 290,978 224,973 170,1010 116,973 50,978 22,918 -38,890 -33,824 -70,770 -33,716 -38,650 22,622 50,562 116,567 170,530 224,567 290,562 318,622 378,650 373,716"/>
      <polygon fill="url(#burst-fill)" stroke="url(#burst-fill)" stroke-width="14" stroke-linejoin="round"
        points="410,770 373,824 378,890 318,918 290,978 224,973 170,1010 116,973 50,978 22,918 -38,890 -33,824 -70,770 -33,716 -38,650 22,622 50,562 116,567 170,530 224,567 290,562 318,622 378,650 373,716"/>
    </svg>

    <h1 class="headline">
      <span class="lead">Explore the</span>
      <span class="lead">Possibilities of</span>
      <span class="feature">CUSTOM APPAREL</span>
      <span class="purpose">FOR UNIFORMING, SPECIAL</span>
      <span class="purpose">EVENTS,TEAM BUILDING AND</span>
      <span class="purpose">MORE.</span>
    </h1>

    <svg class="chevrons" width="55" height="90" viewBox="0 0 55 90" aria-hidden="true">
      <path d="M0,0 L28,45 L0,90 L12,90 L40,45 L12,0 Z" fill="#ffe35a"/>
      <path d="M14,0 L42,45 L14,90 L26,90 L54,45 L26,0 Z" fill="#ffd400"/>
    </svg>

    <ul class="service-list">
      <li>Embroidery</li>
      <li>DTG Printing</li>
      <li>Rhinestones</li>
      <li>Spancjles</li>
      <li>Sublimation</li>
      <li>Vinyl Lettering</li>
      <li>Decals</li>
      <li>Fund Raisers</li>
      <li>Team And Business<br>Logos</li>
      <li>Special Events</li>
      <li>Bridal Showers</li>
      <li>Family Reunions</li>
      <li>Promotional<br>Products</li>
      <li>Monogramincj</li>
      <li>We Make Good<br>Stuff Better!</li>
    </ul>

    <p class="welcome">Emergencies and<br>small orders<br>welcome</p>

    <div class="product tee" role="img" aria-label="Photo of a black tee shirt with company name and logo"></div>
    <div class="product polo" role="img" aria-label="Photo of a white polo shirt with company logo"></div>
    <div class="product coveralls" role="img" aria-label="Photo of khaki work coveralls, front and back"></div>
    <div class="product cap" role="img" aria-label="Photo of a black baseball cap with logo"></div>

    <p class="promo"><span class="discount">10% off</span>and no setup Fees with this promotional code – K-382</p>

    <div class="brand">
      <span class="mark" aria-hidden="true"></span>
      <p class="name">Under The Lantern<br>Tailored Garments and Extras, LLC</p>
    </div>

    <p class="contact">Email: underthelantern@mailtrove.example<br>Website: www.tailoredgarmentsandextras.example<br>www.underthelantern.example</p>
    <p class="address">27852 Falvinter Road<br>Cypress, Texas 77519<br>Tel. (281) 555-0187</p>
  </article>
</body>
</html>
```